Fun conversation piece for the home depicting the history of the ownership (title) and more!

We need some ideas for a framed display to be hung in a home for a new company I started called Wanderlane Keepsakes, LLC. We will create framed (or unframed canvass) wall displays depicting the History of the Home (title transfers) with some interesting background on the subdivision the home is located. This will be a conversation piece. Use color if you feel that works best. I am envisioning perhaps the writing to be in old English or old Spanish font to reflect the history of Florida where I am located. I am wanting to incorporate perhaps a picture of the home converted into sketch as a background to the "history". Or we could skip that and use the vegetation (trees) native to the area for a background. I am going to attach something I found online as a sample but I am open to ideas. The sample is a little formal for what I am trying to do. I may sell these framed or as unframed canvass pictures which might need to be a bit more contemporary. I also need a logo if you have any ideas. WK in some form of old English style perhaps? The document attached labeled "Marlowbrook" is an example of the content I will be creating for the picture.

I misspelled "States" in one of the paragraphs. Can you correct that for me? United States. Not "sates". My bad.

Logo Text

Wanderlane Keepsakes (or WK). Surprise me.

```html
<!DOCTYPE html>
<html lang="en">
<head>
<meta charset="utf-8">
<title>Marlowbrook – Wanderlane Keepsakes</title>
<link rel="stylesheet" href="https://fonts.googleapis.com/css2?family=Almendra:wght@400;700&family=Rye&display=swap">
<style>
  :root {
    --wine: #8b1e1b;
    --wine-dark: #6e1512;
    --ink: #2a1a16;
    --mauve: #c7a7a8;
    --blush: #e2cfcb;
    --sand: #ead8bd;
    --cream: #f1e4d6;
  }
  * { margin: 0; padding: 0; box-sizing: border-box; }
  html, body { width: 848px; height: 1200px; overflow: hidden; background: var(--cream); }
  .poster {
    position: relative;
    width: 848px; height: 1200px;
    overflow: hidden;
    font-family: "Almendra", serif;
    color: var(--ink);
  }
  .backdrop {
    position: absolute; inset: 0;
    background:
      radial-gradient(ellipse 520px 420px at 520px 260px, rgba(236,214,176,0.9), rgba(236,214,176,0) 70%),
      radial-gradient(ellipse 420px 300px at 420px 620px, rgba(226,200,170,0.7), rgba(226,200,170,0) 70%),
      linear-gradient(180deg, var(--mauve) 0%, var(--blush) 55%, #e6d2cf 100%);
  }
  .frame {
    position: absolute; inset: 0;
  }
  .title {
    position: absolute;
    top: 118px; left: 0; width: 848px;
    text-align: center;
    font-family: "Rye", serif;
    font-size: 84px;
    font-weight: 400;
    color: var(--wine);
    letter-spacing: 1px;
  }
  .intro {
    position: absolute;
    top: 344px; left: 128px; width: 592px;
    text-align: center;
    font-size: 10.6px;
    line-height: 21px;
  }
  .intro .lead { color: var(--wine); font-weight: 700; font-size: 14px; }
  .intro .narrow { display: block; padding: 0 40px; }
  .history-heading {
    position: absolute;
    top: 664px; left: 0; width: 848px;
    text-align: center;
    font-size: 24px;
    font-weight: 400;
    color: var(--wine-dark);
  }
  .title-chain {
    position: absolute;
    top: 712px; left: 135px;
    border-collapse: collapse;
    font-size: 17px;
  }
  .title-chain td { padding: 0; height: 24.5px; vertical-align: middle; }
  .title-chain .date { width: 242px; }
  .brand {
    position: absolute;
    top: 970px; left: 0; width: 848px;
    display: flex; align-items: center; justify-content: center; gap: 12px;
    font-size: 24px;
    color: var(--wine);
    padding-left: 190px;
  }
  .brand-dot {
    width: 22px; height: 22px; border-radius: 50%;
    background: var(--wine);
  }
</style>
</head>
<body>
<main class="poster">
  <div class="backdrop" role="img" aria-label="Faded sketch of a mid-century home beneath tall pines and oaks"></div>

  <svg class="frame" width="848" height="1200" viewBox="0 0 848 1200" aria-hidden="true">
    <path d="M150 70 Q424 20 700 70 Q790 90 790 200 L790 1040 Q790 1150 690 1160 L160 1160 Q60 1150 60 1040 L60 200 Q60 90 150 70 Z"
          fill="none" stroke="var(--wine)" stroke-width="14"/>
    <path d="M158 88 Q424 42 692 88 Q770 106 770 204 L770 1036 Q770 1132 684 1140 L166 1140 Q80 1132 80 1036 L80 204 Q80 106 158 88 Z"
          fill="none" stroke="var(--wine)" stroke-width="3"/>
  </svg>

  <h1 class="title">Marlowbrook</h1>

  <p class="intro">
    <span class="lead">Marlowbrook</span> is a neighborhood in the City of Corvella. Located east of Cedar Rise, Marlowbrook is bordered by
    4th Avenue to the west and 7th Avenue and Heron's Creek to the east. Initially developed in 1954, an addition was
    added in 1956. It is located in a beautiful area of America's 1st Settlement (1559), Corvella, Florida encompassed with towering pine trees and breathtaking heritage oaks.<br>
    The land comprising Marlowbrook was originally owned by Mateo Alvarado under a Spanish Land Grant and affirmed by President Elias Thornbury on September 7, 1835. Spain relinquished Florida to the United States in 1819 under the
    <span class="narrow">Harlow-Vega Treaty and lands previously granted to settlers prior thereto were honored if claims were filed and approved by the United States government.</span>
    Through the years, the land changed hands many times but was eventually developed into the Marlowbrook subdivision in 1954, by Walter Haskins, President of Marlowbrook, Inc.<br>
    The subdivision contains 63 lots with a beautiful, oak-filled park located just off of Linden Street.<br>
    Built in 1957 and containing approximately 2606 square feet of living, garage and patio space,
    the home located at 417 Juniper Street is a trip back in time to when houses were carefully planned
    catering to modern sensibilities, neither too big nor too small, neither too formal nor too casual.
  </p>

  <h2 class="history-heading">Wanderlane Keepsakes</h2>

  <table class="title-chain">
    <tr><td class="date">September 9, 1835</td><td>Mateo Alvarado, Spanish Land Grant</td></tr>
    <tr><td class="date">April 27, 1954</td><td>Marlowbrook Plat approved by Bellhaven County</td></tr>
    <tr><td class="date">April 29, 1957</td><td>Walter Haskins, III and Doris M. Haskins</td></tr>
    <tr><td class="date">September 20, 1960</td><td>Loretta Jean Pruitt (Calloway)</td></tr>
    <tr><td class="date">February 11, 1966</td><td>Harold T. Whitcomb and Edna R. Whitcomb</td></tr>
    <tr><td class="date">January 20, 1995</td><td>Dennis K. Hollis</td></tr>
    <tr><td class="date">September 1, 2020</td><td>Dennis K. Hollis and Martin Edward Caldwell</td></tr>
  </table>

  <div class="brand">
    <span class="brand-dot"></span>
    <span class="brand-name">Wanderlane Keepsakes, LLC</span>
  </div>
</main>
</body>
</html>
```